Webdesign für Onlinehändler für Pools
Zielgruppe
Wir sind ein Onlinehändler für Pools. Hauptsächlich bieten wir Poolwasserpflege auf Chemiebasis, Poolzubehör und Pooltechnik. Unsere Zielgruppe sind besitzer von einem Pool im Sommer.
Aufgabenstellung
Wir sind völlig frei in der Vorstellung. Wir wollen unsere Website moderner und neu gestalten. Dafür möchten wir die Startseite vollständig neu designen (Header-Bereich, Hauptbereich und Footer). Die Shopkategorienamen sollen jedoch gleich bleiben. Gerne in cleaner Ausführung. Ach ja, auch wenn ich ein Logo hinzugefügt habe, wäre ich einer anderen Vision des Logos nicht gänzlich abgeneigt und bin hier offen. Eine spätere Zuzahlung für das Logo ist gerne möglich.

```html
<!DOCTYPE html>
<html lang="de">
<head>
<meta charset="utf-8">
<title>Aquaris Poolshop – Startseite</title>
<link href="https://fonts.googleapis.com/css2?family=Manrope:wght@400;500;600;700&display=swap" rel="stylesheet">
<style>
:root{
  --blue:#2b6ea6;
  --red:#e65a3c;
  --text:#3a4550;
  --heading:#4a5560;
  --muted:#8a949d;
  --bg:#f3f5f8;
  --card:#ffffff;
  --wood:#8a6a45;
  --grass:#4f7a38;
}
*{box-sizing:border-box;margin:0;padding:0}
html,body{width:1200px;height:2405px;overflow:hidden;background:var(--bg)}
body{font-family:'Manrope',sans-serif;color:var(--text);font-size:13px}
.page{width:1200px;height:2405px;padding:0 120px;overflow:hidden;position:relative}
svg.ic{width:14px;height:14px;stroke:var(--blue);fill:none;stroke-width:1.8;vertical-align:-2px}
/* header */
.topbar{height:58px;display:flex;align-items:center;justify-content:space-between}
.brand{display:flex;align-items:center;gap:8px;font-weight:700;font-size:20px;color:var(--blue)}
.brand .dot{width:26px;height:26px;border-radius:50%;background:var(--red)}
.contact{color:var(--blue);font-size:13px;display:flex;gap:6px;align-items:center}
.social{display:flex;gap:8px}
.social span{width:10px;height:10px;border-radius:50%;background:var(--blue)}
.navbar{height:42px;display:flex;align-items:center;gap:28px}
.cats{font-weight:600;display:flex;align-items:center;gap:6px}
.cats::before{content:"";width:6px;height:6px;border-radius:50%;background:var(--red)}
.search{flex:1;height:30px;background:var(--card);border-radius:4px;display:flex;align-items:center;justify-content:space-between;padding:0 12px;color:#b8bfc6}
.tools{display:flex;gap:10px;align-items:center;position:relative}
.badge{position:absolute;right:-8px;top:-6px;width:12px;height:12px;border-radius:50%;background:var(--red);color:#fff;font-size:8px;text-align:center;line-height:12px}
/* hero */
.hero{display:grid;grid-template-columns:700px 240px;gap:20px;height:420px;margin-top:6px}
.hero-left{display:flex;flex-direction:column;gap:16px}
.welcome{background:var(--card);height:96px;padding:14px 14px;border-radius:4px}
.welcome h1{font-weight:500;font-size:32px;line-height:1.1;color:var(--heading)}
.welcome h1 span{display:block;color:var(--blue)}
.photo{border-radius:4px;position:relative}
.hero-main{flex:1;background:linear-gradient(180deg,#5b7a48 0%,#6fa0c0 35%,#4b95c8 50%,var(--wood) 62%,#6e5236 80%,var(--grass) 100%)}
.tag{position:absolute;left:10px;bottom:10px;background:rgba(255,255,255,.88);padding:6px 10px;font-size:12px;line-height:1.3;color:#555;width:250px}
.tag b{color:var(--blue);font-weight:600;float:right}
.hero-right{display:flex;flex-direction:column;gap:20px}
.side-top{height:200px;background:linear-gradient(180deg,#4a6d3a 0%,#7a5c3e 45%,#3d8dc0 60%,#7a5c3e 78%,#5a8a40 100%)}
.side-bot{flex:1;background:var(--card);display:flex;flex-direction:column}
.side-bot .shot{flex:1;margin:12px;background:radial-gradient(circle at 50% 55%,#d4e63a 0%,#b7cc30 30%,#2a2e30 55%,#ffffff 75%)}
.side-bot .tag{position:static;width:auto;margin:0 10px 10px;background:none}
/* sections */
h2{font-weight:500;font-size:25px;color:var(--heading);margin:18px 0 10px;line-height:1.2}
.carousel{background:var(--card);height:170px;display:flex;align-items:center;padding:0 14px;gap:24px;border-radius:4px}
.arrow{color:var(--blue);font-size:22px;width:14px}
.cat{width:190px;text-align:center;font-size:12px}
.cat .img{height:130px;margin-bottom:8px}
.c1{background:linear-gradient(160deg,#bfe2f2,#3ba2d6 60%,#1c76ad)}
.c2{background:linear-gradient(160deg,#3a7fc4,#e6b82a 45%,#2b2f33 70%,#dfe3e6)}
.c3{background:linear-gradient(160deg,#e8ecef,#3a88c8 40%,#2a2e33 70%,#cfd6db)}
.c4{background:linear-gradient(160deg,#6ab5d8,#2d6fc4 45%,#ffffff 80%)}
.offers{display:grid;grid-template-columns:380px repeat(3,174px);gap:22px;margin-top:26px;height:180px}
.offer-box{background:var(--card);padding:40px 16px 0}
.offer-box h3{font-weight:500;font-size:24px;color:var(--heading)}
.offer-box p{font-size:16px;margin:6px 0 12px}
.btn-red{display:inline-block;background:var(--red);color:#fff;font-size:12px;padding:4px 8px}
.btn-blue{display:inline-block;background:var(--blue);color:#fff;font-size:12px;padding:4px 8px}
.pcard{background:var(--card);position:relative;padding:26px 10px 8px;font-size:11px;color:var(--muted)}
.sale{position:absolute;left:8px;top:8px;background:var(--red);color:#fff;font-size:10px;padding:1px 6px}
.heart{position:absolute;right:8px;top:6px;color:var(--blue);font-size:15px}
.pimg{height:74px;width:64px;margin:0 auto 8px;background:linear-gradient(160deg,#f4f6f8,#c9d5df);border-radius:3px}
.pimg.can{background:linear-gradient(160deg,#3aa0e0,#1568b8);width:58px}
.pimg.bottle{background:linear-gradient(180deg,#9aa2a8 0 25%,#eef1f3 25%);width:34px}
.pimg.jug{background:linear-gradient(160deg,#3a6fe0,#0f3aa8);width:60px}
.pimg.white{background:linear-gradient(180deg,#4a9fd8 0 18%,#f5f7f9 18%);width:50px}
.pname{color:#6a737b;line-height:1.3}
.price{margin-top:4px;font-weight:600;color:var(--blue)}
.price s{color:var(--muted);font-weight:500;margin-right:8px}
.unit{font-size:8px;color:#b0b7bd}
.perks{display:grid;grid-template-columns:repeat(3,1fr);gap:26px}
.perk{background:var(--card);height:62px;display:flex;align-items:center;gap:14px;padding:0 12px}
.perk svg{width:38px;height:38px;stroke:var(--blue);fill:none;stroke-width:1.8;flex:none}
.perk b{display:block;color:var(--blue);font-weight:600;font-size:12px}
.perk span{font-size:12px;color:var(--muted);line-height:1.2}
.best{display:grid;grid-template-columns:340px repeat(3,1fr);grid-template-rows:184px 184px;gap:20px}
.best .big{grid-row:1/3;background:var(--card);position:relative;padding:34px 16px 16px}
.big h4{font-weight:500;font-size:22px;line-height:1.2}
.big .price{font-size:20px;font-weight:500}
.big .pimg{height:200px;width:120px;margin:12px auto 16px}
.news{display:grid;grid-template-columns:460px 1fr;margin-top:28px;height:168px;background:var(--card)}
.news-text{padding:20px 16px}
.news-text h3{font-weight:500;font-size:25px;color:var(--heading)}
.news-text p{font-size:12px;color:var(--muted);margin:10px 0 18px;line-height:1.3;width:340px}
.news-form{display:flex;gap:20px;align-items:center}
.email{width:250px;height:26px;border:1px solid #c9d0d6;font-size:12px;color:#b5bcc2;padding:4px 10px}
.news-img{background:linear-gradient(110deg,#c9b27a,#8a6a48 40%,#e8d8b8 70%,#a58a64)}
.blog{display:grid;grid-template-columns:repeat(3,1fr);gap:22px}
.post .img{height:140px}
.b1{background:linear-gradient(180deg,#cfd8de,#8a6e58 45%,#4a8fc2 70%,#e8edf0)}
.b2{background:linear-gradient(160deg,#6aa844,#cfe6b6 50%,#3e7a2e)}
.b3{background:linear-gradient(160deg,#5f9e3a,#9ccf55 50%,#3e6f2a)}
.meta{font-size:9px;color:#a0a8ae;margin:6px 8px 2px;display:flex;gap:12px}
.post p{font-size:12px;margin:0 8px;line-height:1.3;height:32px}
.more{text-align:right;color:var(--blue);font-size:12px;margin:6px 10px 0}
footer{margin-top:26px;padding-top:14px}
.fgrid{display:grid;grid-template-columns:290px 195px 290px 1fr;height:180px}
.fgrid h5{color:var(--blue);font-size:13px;font-weight:600;margin-bottom:8px}
.fgrid li{list-style:none;font-size:12px;color:#6a737b;line-height:1.5}
.addr{margin-top:22px;font-size:12px;line-height:1.5;color:#5a646d}
.pay{display:grid;grid-template-columns:auto auto auto;gap:6px 12px;font-size:12px;color:var(--heading);margin-bottom:18px}
.pay span::before{content:"";display:inline-block;width:8px;height:8px;background:var(--heading);margin-right:4px}
.fbar{border-top:1px solid var(--muted);display:flex;justify-content:space-between;padding-top:8px;font-size:12px;color:#5a646d}
.fbar div{display:flex;gap:40px}
</style>
</head>
<body>
<div class="page">
  <header>
    <div class="topbar">
      <div class="brand"><span class="dot"></span>Aquaris Poolshop</div>
      <div class="contact"><svg class="ic" viewBox="0 0 24 24"><path d="M5 3h4l2 5-3 2a11 11 0 0 0 6 6l2-3 5 2v4a2 2 0 0 1-2 2A18 18 0 0 1 3 5a2 2 0 0 1 2-2z"/></svg>0987 654 321 0</div>
      <div class="contact"><svg class="ic" viewBox="0 0 24 24"><rect x="3" y="5" width="18" height="14"/><path d="M3 5l9 8 9-8"/></svg>info@aquaris-poolshop.de</div>
      <div class="social"><span></span><span></span><span></span></div>
    </div>
    <div class="navbar">
      <div class="cats">Kategorien</div>
      <div class="search">Suche…<svg class="ic" viewBox="0 0 24 24"><circle cx="10" cy="10" r="6"/><path d="M15 15l5 5"/></svg></div>
      <div class="tools">
        <svg class="ic" viewBox="0 0 24 24"><circle cx="12" cy="8" r="4"/><path d="M4 21c1-5 15-5 16 0"/></svg>
        <svg class="ic" viewBox="0 0 24 24"><path d="M12 20l-8-8a5 5 0 0 1 8-6 5 5 0 0 1 8 6z"/></svg>
        <svg class="ic" viewBox="0 0 24 24"><path d="M2 3h3l3 12h12l2-8H6"/><circle cx="9" cy="20" r="1.5"/><circle cx="18" cy="20" r="1.5"/></svg>
        <span class="badge">2</span>
      </div>
    </div>
  </header>

  <section class="hero">
    <div class="hero-left">
      <div class="welcome"><h1>WILLKOMMEN IM AQUARIS-POOLSHOP<span>IHR POOLSHOP FÜR DEN BADESPAß</span></h1></div>
      <div class="photo hero-main" role="img" aria-label="Rechteckiger Holzpool im Garten mit badenden Kindern">
        <div class="tag">Holmar Pool Komplettset aus<br>Echtholz Salvia Rechteck<br>1010 x 418 x 146 cm <b>1244,49 €</b></div>
      </div>
    </div>
    <div class="hero-right">
      <div class="photo side-top" role="img" aria-label="Runder Holzpool im Garten">
        <div class="tag" style="width:auto;right:10px">Holmar Rundformbeckenset<br>Holzoptik Marina<br>Ø 240 x 120 cm <b>1244,49 €</b></div>
      </div>
      <div class="side-bot">
        <div class="shot" role="img" aria-label="Gelb-schwarzer Poolroboter"></div>
        <div class="tag">Poolroboter Wellix<br>Vario Eco <b>2129,00 €</b></div>
      </div>
    </div>
  </section>

  <h2>TOP KATEGORIEN</h2>
  <section class="carousel">
    <span class="arrow">‹</span>
    <div class="cat"><div class="img c1" role="img" aria-label="Pflegemittel wird ins Poolwasser gegeben"></div>WASSERPFLEGE</div>
    <div class="cat"><div class="img c2" role="img" aria-label="Poolroboter am Beckenboden"></div>POOLROBOTER</div>
    <div class="cat"><div class="img c3" role="img" aria-label="Sandfilteranlagen"></div>SANDFILTERANLAGEN</div>
    <div class="cat"><div class="img c4" role="img" aria-label="Kanister mit Überwinterungsmittel am Pool"></div>ÜBERWINTERUNG</div>
    <span class="arrow">›</span>
  </section>

  <section class="offers">
    <div class="offer-box"><h3>AKTUELLE ANGEBOTE</h3><p>Nur solange der Vorrat reicht</p><span class="btn-red">Zu den Angeboten %</span></div>
    <div class="pcard"><span class="sale">% SALE</span><span class="heart">♡</span><div class="pimg" role="img" aria-label="Produktpackung"></div><div class="pname">4 x 35g - Clarova<br>Wasser-Rein</div><div class="price"><s>15,00 €</s>13,00 €</div><div class="unit">1 kg = 92,86 €</div></div>
    <div class="pcard"><span class="sale">% SALE</span><span class="heart">♡</span><div class="pimg" role="img" aria-label="Produktpackung"></div><div class="pname">4 x 35g - Clarova<br>Wasser-Rein</div><div class="price"><s>15,00 €</s>13,00 €</div><div class="unit">1 kg = 92,86 €</div></div>
    <div class="pcard"><span class="sale">% SALE</span><span class="heart">♡</span><div class="pimg" role="img" aria-label="Produktpackung"></div><div class="pname">4 x 35g - Clarova<br>Wasser-Rein</div><div class="price"><s>15,00 €</s>13,00 €</div><div class="unit">1 kg = 92,86 €</div></div>
  </section>

  <h2>IHRE VORTEILE BEI UNS</h2>
  <section class="perks">
    <div class="perk"><svg viewBox="0 0 40 40"><path d="M10 30V8a4 4 0 0 1 8 0M24 30V8a4 4 0 0 1 8 0M10 14h14M10 22h14M4 34q4-3 8 0t8 0 8 0 8 0"/></svg><div><b>FACHHANDEL</b><span>Seit 1996 Fachhandel für<br>Pool-Artikel</span></div></div>
    <div class="perk"><svg viewBox="0 0 40 40"><path d="M8 18l12-8 12 12-12 10zM8 18l12 14M20 10l4 10M30 30q2 4 4 0"/></svg><div><b>FRISCH ABGEFÜLLT</b><span>Hochwertige und frisch<br>abgefüllte Produkte</span></div></div>
    <div class="perk"><svg viewBox="0 0 40 40"><rect x="4" y="18" width="7" height="16"/><path d="M11 20l7-12q4 0 3 6l-1 4h10a3 3 0 0 1 2 4l-3 10a3 3 0 0 1-3 2H11"/></svg><div><b>MARKENQUALITÄT</b><span>Preiswerte Markenqualität<br>deutscher Hersteller</span></div></div>
  </section>

  <h2>UNSERE BESTSELLER</h2>
  <section class="best">
    <div class="big"><span class="sale">% SALE</span><span class="heart">♡</span><h4>1 kg - Clarova Chlor-<br>Granulat</h4><div class="price"><s>25,00 €</s>21,10 €</div><div class="unit">1 kg = 21,10 €</div><div class="pimg bottle" role="img" aria-label="Dose Chlor-Granulat" style="width:120px"></div><span class="btn-blue">In den Warenkorb</span></div>
    <div class="pcard"><span class="heart">♡</span><div class="pimg" role="img" aria-label="Produktpackung"></div><div class="pname">4 x 35g - Clarova<br>Wasser-Rein</div><div class="price">13,00 €</div><div class="unit">1 kg = 92,86 €</div></div>
    <div class="pcard"><span class="heart">♡</span><div class="pimg can" role="img" aria-label="Blauer Kanister"></div><div class="pname">20 l - Aquelo -<br>Chlor-Flüssig Aktiv</div><div class="price">67,45 €</div><div class="unit">1 l = 3,37 €</div></div>
    <div class="pcard"><span class="heart">♡</span><div class="pimg white" role="img" aria-label="Weißer Kanister"></div><div class="pname">20 l - Aquelo pH-Senker<br>Flüssig 14,9%</div><div class="price">66,55 €</div><div class="unit">1 l = 3,33 €</div></div>
    <div class="pcard"><span class="sale">% SALE</span><span class="heart">♡</span><div class="pimg" role="img" aria-label="Produktpackung"></div><div class="pname">4 x 35g - Clarova<br>Wasser-Rein</div><div class="price"><s>15,00 €</s>13,00 €</div><div class="unit">1 kg = 92,86 €</div></div>
    <div class="pcard"><span class="heart">♡</span><div class="pimg bottle" role="img" aria-label="Flasche Klärmittel"></div><div class="pname">1 l - Clarova Klar-<br>Wasser</div><div class="price">21,10 €</div><div class="unit">1 l = 21,10 €</div></div>
    <div class="pcard"><span class="heart">♡</span><div class="pimg jug" role="img" aria-label="Blauer Kanister"></div><div class="pname">24,5 kg - Blaufix<br>Chlor-Flüssig</div><div class="price">64,90 €</div><div class="unit">1 kg = 2,65 €</div></div>
  </section>

  <section class="news">
    <div class="news-text">
      <h3>NEWSLETTER</h3>
      <p>Abonniere unseren Newsletter und erhalte einen <b>10 % Gutschein</b> für deinen ersten Einkauf bei uns.</p>
      <div class="news-form"><div class="email">E-Mail</div><span class="btn-blue">10 % sparen →</span></div>
    </div>
    <div class="news-img" role="img" aria-label="Hände halten ein Smartphone mit Briefsymbolen"></div>
  </section>

  <h2>AKTUELL IN UNSEREM BLOG</h2>
  <section class="blog">
    <article class="post"><div class="img b1" role="img" aria-label="Verschneiter Pool vor einer Holzhütte"></div><div class="meta"><span>Aquaris Poolshop</span><span>4. November 2022</span><span>12</span></div><p>Pool im Winter nutzen: So klappt es</p><div class="more">weiterlesen →</div></article>
    <article class="post"><div class="img b2" role="img" aria-label="Gartendusche zwischen grünen Pflanzen"></div><div class="meta"><span>Aquaris Poolshop</span><span>1. Juli 2022</span><span>12</span></div><p>Duschen im Garten: Diese Möglichkeiten gibt es</p><div class="more">weiterlesen →</div></article>
    <article class="post"><div class="img b3" role="img" aria-label="Pool mit grünem Algenwasser"></div><div class="meta"><span>Aquaris Poolshop</span><span>31. März 2022</span><span>12</span></div><p>Algen im Pool – Vorbeugende Maßnahmen und erste Hilfe</p><div class="more">weiterlesen →</div></article>
  </section>

  <footer>
    <div class="fgrid">
      <div>
        <div class="brand"><span class="dot"></span>Aquaris Poolshop</div>
        <div class="addr">Aquaris Poolshop GmbH<br>Seeweg 7<br>12345 Lindenau<br>0987 654 321 0<br>info@aquaris-poolshop.de</div>
      </div>
      <div><h5>Informationen</h5><ul><li>Bonuspunkte</li><li>FAQ</li><li>Versandkosten</li><li>Bestellung &amp; Zahlung</li><li>Newsletter</li><li>Informationsbroschüre</li><li>Batterieentsorgung</li><li>Unser Blog</li></ul></div>
      <div><h5>Service</h5><ul><li>Kontakt</li><li>Widerrufsrecht</li><li>AGB &amp; Kundenkonto</li><li>AGB Bonuspunkteprogramm</li></ul></div>
      <div><h5>Zahlungsarten</h5>
        <div class="pay"><span>Paynova</span><span>Kartix</span><span>Zahlfix</span><span>Paynova</span><span>Kartix</span><span>Zahlfix</span></div>
        <h5>Folgen Sie uns</h5><div class="social"><span></span><span></span><span></span></div>
      </div>
    </div>
    <div class="fbar"><span>© 2024 Aquaris Poolshop GmbH</span><div><span>Impressum</span><span>Datenschutz</span></div></div>
  </footer>
</div>
</body>
</html>
```